"Love Your Feet" Post Card

Hi,
We are looking to send out a postcard campaign to our current patients through Brightleaf Press. We are a foot and ankle doctor's office (Podiatrists). The goal is to get a design to remind them to care for their feet and that we can help them if they have any foot or ankle issues.
We are aiming for the patients to look at the postcard and have them remind themselves that they need to get their feet checked out.

Aiming to have these ready by the last week of January to be mailed out to arrive at their doorsteps by Valentines Day.

Postcard Size: 4.2" x 5.5" See attached for front and back requirements
backside needs to leave space for mailing address and stamp.
Our font is: Quorum
Our address:
386 Marlowe Creek Rd.
Ste. 420
Frederick, MD 21745

Thank you,

Target Market(s)

Our median age for patients range from 40 - 60 years of age.

Industry/Entity Type

Medical / Healthcare

Requirements
Must have
• Our address since it's a postcard

```html
<!DOCTYPE html>
<html lang="en">
<head>
<meta charset="utf-8">
<title>Love Your Feet Postcard</title>
<link rel="stylesheet" href="https://fonts.googleapis.com/css2?family=Parisienne&family=Gilda+Display&display=swap">
<style>
  :root {
    --backdrop: #d2d2d2;
    --paper: #eeeeec;
    --aqua: #95e5e3;
    --aqua-deep: #7fd3d1;
    --ink: #2e2828;
  }
  html, body {
    margin: 0;
    padding: 0;
    width: 1200px;
    height: 800px;
    overflow: hidden;
    background: var(--backdrop);
  }
  .postcard {
    position: absolute;
    left: 100px;
    top: 18px;
    width: 1000px;
    height: 764px;
    background: var(--paper);
    overflow: hidden;
  }
  .postcard__band {
    position: absolute;
    inset: 0;
    width: 1000px;
    height: 764px;
  }
  .postcard__band polygon { fill: var(--aqua); }
  .tagline {
    position: absolute;
    left: 88px;
    top: 62px;
    margin: 0;
    font-family: "Parisienne", cursive;
    font-weight: 400;
    font-size: 46px;
    line-height: 72px;
    color: var(--ink);
  }
  .feet-artwork {
    position: absolute;
    left: 120px;
    top: 275px;
    width: 300px;
    height: 265px;
    border-radius: 40% 40% 45% 45%;
    background: var(--aqua-deep);
  }
  .address {
    position: absolute;
    left: 560px;
    top: 270px;
    margin: 0;
    font-family: "Gilda Display", serif;
    font-style: normal;
    font-size: 31px;
    line-height: 50px;
    color: var(--ink);
  }
</style>
</head>
<body>
  <main class="postcard">
    <svg class="postcard__band" viewBox="0 0 1000 764" aria-hidden="true">
      <polygon points="0,0 780,0 780,237 510,237 510,634 126,634 126,764 0,764"/>
    </svg>
    <p class="tagline">Self love is taking care of yourself,<br>starting with your feet.</p>
    <div class="feet-artwork" role="img" aria-label="Illustration of two small footprints inside an outlined heart, with little red hearts by the toes"></div>
    <address class="address">
      386 Marlowe Creek Rd.<br>
      Ste. 420<br>
      Frederick, MD 21745
    </address>
  </main>
</body>
</html>
```